Conservative, Modern and Sharp Builder Business card

Hi there,
We would like to update our existing business card.
I have attached photos of existing business card, logo and van sign.

I would like the business card to also list what we do :
Renovation • New Build • Alteration
Extension • Bathroom • Maintenance.(Seperated by dots)

Contact number : 021 0483 0752
(With that exact spacing)

Ideally when people looking from about 2-3 metres, they know that it is a builder’s business card

Open to suggestions on fonts, layout, style of business card

PLEASE ONLY SUBMIT YOUR BEST OR MAX 3 DESIGNS FOR EACH DESIGNER

Thanks

Industry/Entity Type

Construction. Renovation

Contact Information for Business Card

Details should be the same as the existing card. And addition of what we do.

Requirements
Should not have
• The new business card must not have the same layout as our existing one. Thanks

```html
<!DOCTYPE html>
<html lang="en">
<head>
<meta charset="UTF-8">
<title>Keelstone Build – Business Card</title>
<link rel="stylesheet" href="https://fonts.googleapis.com/css2?family=Arimo:wght@400;700&display=swap">
<style>
  :root{
    --stage:#e8e8e8;
    --card:#2b2b2b;
    --ink:#f4f4f4;
    --ink-soft:#cfcfcf;
    --rule:#8a8a8a;
    --glow:#3a3a3a;
    --shade:#1e1e1e;
  }
  *{box-sizing:border-box;margin:0;padding:0}
  html,body{width:1200px;height:801px;overflow:hidden;background:var(--stage)}
  body{font-family:"Arimo",Arial,sans-serif;color:var(--ink);position:relative}
  .card{
    position:absolute;top:245px;width:540px;height:310px;
    background:var(--card);border-radius:4px;overflow:hidden;
    box-shadow:0 8px 22px rgba(0,0,0,.25);
  }
  .card--contact{left:40px}
  .card--services{left:620px}

  .brand{display:flex;align-items:center;gap:10px;font-weight:700;color:var(--ink);letter-spacing:.5px;white-space:nowrap}
  .brand__square{width:12px;height:12px;background:var(--ink);flex:none}

  /* contact side */
  .card--contact .brand{position:absolute;right:36px;top:52px;font-size:38px}
  .divider{position:absolute;left:36px;right:36px;top:150px;height:1px;background:var(--rule)}
  .person{position:absolute;left:36px;top:176px;width:250px}
  .person__name{font-size:19px;font-weight:700;letter-spacing:1px;text-transform:uppercase}
  .person__role{font-size:15px;color:var(--ink-soft);margin-top:4px}
  .person__rule{height:1px;background:var(--rule);margin:10px 0;width:200px}
  .contact-line{display:flex;align-items:center;gap:8px;font-size:15px;color:var(--ink-soft);margin-bottom:6px;white-space:nowrap}
  .contact-line svg{width:13px;height:13px;flex:none}
  .online{position:absolute;right:36px;top:176px}

  /* services side */
  .emblem-field{
    position:absolute;inset:0;
    background:
      radial-gradient(ellipse 300px 240px at 32% 52%,var(--glow) 0%,rgba(58,58,58,0) 70%),
      linear-gradient(115deg,var(--shade) 0%,var(--card) 45%,var(--card) 100%);
  }
  .services-block{position:absolute;right:34px;top:62px;width:280px;text-align:center}
  .card--services .brand{justify-content:center;font-size:32px}
  .services{margin-top:30px;font-size:17px;line-height:1.55;color:var(--ink);white-space:nowrap}
</style>
</head>
<body>

<section class="card card--contact" aria-label="Business card, contact side">
  <div class="brand"><span class="brand__square"></span>Keelstone Build</div>
  <div class="divider"></div>

  <div class="person">
    <p class="person__name">Marten Oduya</p>
    <p class="person__role">Residential Builder</p>
    <div class="person__rule"></div>
    <p class="contact-line">
      <svg viewBox="0 0 16 16" aria-hidden="true"><path d="M4 1.5l2.5 3-1.5 2a9 9 0 0 0 4.5 4.5l2-1.5 3 2.5-1.5 2.5C7 14.5 1.5 9 1.5 3z" fill="none" stroke="currentColor" stroke-width="1.4"/></svg>
      021 0483 0752
    </p>
    <p class="contact-line">
      <svg viewBox="0 0 16 16" aria-hidden="true"><rect x="1.5" y="3.5" width="13" height="9" fill="none" stroke="currentColor" stroke-width="1.4"/><path d="M1.5 3.5L8 9l6.5-5.5" fill="none" stroke="currentColor" stroke-width="1.4"/></svg>
      hello@keelstonebuild.nz
    </p>
  </div>

  <div class="online">
    <p class="contact-line">
      <svg viewBox="0 0 16 16" aria-hidden="true"><circle cx="8" cy="8" r="6.5" fill="none" stroke="currentColor" stroke-width="1.4"/><path d="M1.5 8h13M8 1.5c-3 3.5-3 9.5 0 13M8 1.5c3 3.5 3 9.5 0 13" fill="none" stroke="currentColor" stroke-width="1.2"/></svg>
      www.keelstonebuild.nz
    </p>
    <p class="contact-line">
      <svg viewBox="0 0 16 16" aria-hidden="true"><circle cx="8" cy="8" r="6" fill="currentColor"/></svg>
      keelstonebuild.nz
    </p>
  </div>
</section>

<section class="card card--services" aria-label="Business card, services side">
  <div class="emblem-field" role="img" aria-label="Large embossed brand emblem decoration across the card"></div>
  <div class="services-block">
    <div class="brand"><span class="brand__square"></span>Keelstone Build</div>
    <p class="services">
      • Renovation • New Build<br>
      • Alteration • Extension<br>
      • Bathroom • Maintenance
    </p>
  </div>
</section>

</body>
</html>
```